Poster design for a company operating care homes in the UK showcasing our core values

We need a poster to display in our care homes showcasing our new core values:

Purpose
We are driven by a clear understanding of why we do what we do: to enrich lives, honour legacies and make a meaningful difference every day, for our residents, their families, our colleagues and our community.

Excellence
We hold ourselves to the highest standards, delivering exceptional care and creating an environment where both residents and staff can thrive.

Openness
We build trust through honest, respectful communication, welcoming feedback, sharing ideas, and embracing change as a path to continuous growth.

Passion
We are passionate about delivering exceptional care. We take pride in what we do and in making a real difference in people’s lives.

Learning
We are committed to personal and professional growth; empowering each other through ongoing development, reflection, and shared knowledge.

Empathy
We actively listen and seek to understand before being understood, recognising the unique stories, feelings, and needs of others.

I have attached a small graphic that we would like you try to incorporate, in addition to our company logo. Please theme the rest of the poster around our company colours.

```html
<!DOCTYPE html>
<html lang="en">
<head>
<meta charset="utf-8">
<title>Our Core Values – Halden</title>
<link rel="stylesheet" href="https://fonts.googleapis.com/css2?family=Poppins:wght@400;600;700&family=Bebas+Neue&display=swap">
<style>
  :root {
    --navy: #41516e;
    --steel: #6f85ad;
    --peach: #dfa98a;
    --blush: #f6e3d8;
    --blush-soft: #fbeee6;
    --paper: #fcfbfa;
    --ink: #1c1c1c;
    --white: #ffffff;
  }
  * { margin: 0; padding: 0; box-sizing: border-box; }
  html, body { width: 848px; height: 1200px; overflow: hidden; background: var(--paper); }
  .poster {
    position: relative; width: 848px; height: 1200px; overflow: hidden;
    background: var(--paper);
    font-family: "Poppins", sans-serif; color: var(--ink);
  }
  .backdrop { position: absolute; inset: 0; }
  .brand {
    position: absolute; left: 68px; top: 50px;
    display: flex; align-items: center; gap: 10px;
    font-family: "Poppins", sans-serif; font-weight: 600;
    font-size: 34px; color: var(--navy); letter-spacing: 0.5px;
  }
  .brand-mark { width: 16px; height: 16px; background: var(--navy); border-radius: 50%; }
  .headline {
    position: absolute; left: 61px; top: 198px;
    font-family: "Poppins", sans-serif; font-weight: 700;
    font-size: 33px; letter-spacing: 0.6px; line-height: 1;
    color: var(--ink);
  }
  .headline .accent { color: var(--navy); }
  .tagline {
    position: absolute; left: 62px; top: 252px;
    font-size: 20.5px; line-height: 25px; font-weight: 400; letter-spacing: 0.5px;
  }
  .values-row { position: absolute; inset: 0; }
  .hex-label { font-family: "Bebas Neue", sans-serif; }
  .values-grid {
    position: absolute; left: 177px; top: 588px;
    display: grid; grid-template-columns: 175px 190px 170px;
    column-gap: 0; row-gap: 30px; color: var(--white);
  }
  .value h2 {
    font-size: 15.5px; font-weight: 700; letter-spacing: 0.6px;
    margin-bottom: 20px; line-height: 20px;
  }
  .value p { font-size: 16.5px; line-height: 20.5px; letter-spacing: 0.3px; }
  .value.row-one { min-height: 250px; }
</style>
</head>
<body>
<main class="poster">
  <svg class="backdrop" width="848" height="1200" viewBox="0 0 848 1200" aria-hidden="true">
    <defs>
      <linearGradient id="photoFade" x1="0" y1="0" x2="1" y2="0">
        <stop offset="0" stop-color="#e9e3dd" stop-opacity="0"/>
        <stop offset="0.25" stop-color="#e3ddd7" stop-opacity="0.85"/>
        <stop offset="1" stop-color="#d9d2cb"/>
      </linearGradient>
    </defs>
    <!-- pale sweeping band -->
    <path d="M-40 760 C 120 470, 560 300, 900 420 L 900 620 C 620 470, 200 560, -40 900 Z" fill="var(--blush)"/>
    <path d="M-40 900 C 200 580, 560 520, 900 640 L 900 560 C 600 460, 160 520, -40 800 Z" fill="var(--blush-soft)"/>
    <!-- top-left white cap with peach arc -->
    <path d="M0 0 L404 0 C 392 120, 250 180, 35 165 L0 160 Z" fill="var(--white)"/>
    <path d="M404 0 C 392 120, 250 180, 35 165" fill="none" stroke="var(--peach)" stroke-width="5"/>
  </svg>

  <svg class="backdrop" width="848" height="1200" viewBox="0 0 848 1200">
    <rect x="380" y="0" width="468" height="405" fill="url(#photoFade)" role="img" aria-label="Photo of a carer in blue scrubs holding hands with a smiling older resident in a wheelchair"/>
    <defs>
      <linearGradient id="photoFade" x1="0" y1="0" x2="1" y2="0">
        <stop offset="0" stop-color="#e9e3dd" stop-opacity="0"/>
        <stop offset="0.3" stop-color="#c9d3df" stop-opacity="0.8"/>
        <stop offset="1" stop-color="#d8cfc5"/>
      </linearGradient>
    </defs>
  </svg>

  <div class="brand"><span class="brand-mark"></span>Halden</div>

  <h1 class="headline">OUR CORE <span class="accent">VALUES</span></h1>
  <p class="tagline">Together, We Create a Home<br>Where Everyone Thrives</p>

  <svg class="values-row" width="848" height="1200" viewBox="0 0 848 1200" aria-label="PEOPLE values acronym">
    <defs>
      <polygon id="hex" points="0,-66 57,-33 57,33 0,66 -57,33 -57,-33" stroke-linejoin="round"/>
    </defs>
    <!-- big navy panel -->
    <path d="M200 527 L655 527 Q668 527 675 537 L860 810 L655 1200 L200 1200 L-12 810 L180 537 Q187 527 200 527 Z" fill="var(--navy)"/>

    <g transform="translate(152 465) rotate(17)">
      <use href="#hex" transform="translate(-12 -4) scale(1.1)" fill="var(--steel)"/>
      <use href="#hex" fill="var(--peach)"/>
    </g>
    <g transform="translate(264 423) rotate(17)">
      <use href="#hex" transform="translate(-12 -4) scale(1.1)" fill="var(--steel)"/>
      <use href="#hex" fill="var(--navy)"/>
    </g>
    <g transform="translate(372 462) rotate(17)">
      <use href="#hex" transform="translate(-12 -4) scale(1.1)" fill="var(--steel)"/>
      <use href="#hex" fill="var(--peach)"/>
    </g>
    <g transform="translate(482 420) rotate(17)">
      <use href="#hex" transform="translate(-12 -4) scale(1.1)" fill="var(--steel)"/>
      <use href="#hex" fill="var(--navy)"/>
    </g>
    <g transform="translate(590 462) rotate(17)">
      <use href="#hex" transform="translate(-12 -4) scale(1.1)" fill="var(--steel)"/>
      <use href="#hex" fill="var(--peach)"/>
    </g>
    <g transform="translate(706 418) rotate(17)">
      <use href="#hex" transform="translate(12 -4) scale(1.1)" fill="var(--steel)"/>
      <use href="#hex" fill="var(--navy)"/>
    </g>

    <g class="hex-label">
      <text x="115" y="483" fill="var(--navy)"><tspan font-size="46">P</tspan><tspan font-size="19">URPOSE</tspan></text>
      <text x="222" y="438" fill="var(--peach)"><tspan font-size="46">E</tspan><tspan font-size="14">XCELLENCE</tspan></text>
      <text x="329" y="480" fill="var(--navy)"><tspan font-size="46">O</tspan><tspan font-size="17">PENNESS</tspan></text>
      <text x="444" y="436" fill="var(--peach)"><tspan font-size="46">P</tspan><tspan font-size="17">ASSION</tspan></text>
      <text x="546" y="477" fill="var(--navy)"><tspan font-size="46">L</tspan><tspan font-size="17">EARNING</tspan></text>
      <text x="657" y="433" fill="var(--peach)"><tspan font-size="46">E</tspan><tspan font-size="17">MPATHY</tspan></text>
    </g>
  </svg>

  <section class="values-grid">
    <article class="value row-one">
      <h2>PURPOSE</h2>
      <p>We enrich lives,<br>honour legacies,<br>and make a<br>meaningful<br>difference every<br>day—for our<br>residents, their<br>families, our<br>colleagues, and<br>our community.</p>
    </article>
    <article class="value row-one">
      <h2>EXCELLENCE</h2>
      <p>We uphold the<br>highest<br>standards in all<br>we do, providing<br>exceptional care<br>and creating an<br>environment<br>where everyone<br>can flourish.</p>
    </article>
    <article class="value row-one">
      <h2>OPENNESS</h2>
      <p>We communicate<br>honestly and<br>respectfully,<br>welcoming<br>feedback, sharing<br>ideas, and<br>embracing<br>positive change.</p>
    </article>
    <article class="value">
      <h2>PASSION</h2>
      <p>We love what we<br>do. Our<br>enthusiasm and<br>dedication shine<br>through in every<br>moment of care<br>we deliver</p>
    </article>
    <article class="value">
      <h2>LEARNING</h2>
      <p>We grow<br>together—commi<br>tted to ongoing<br>development,<br>reflection, and<br>sharing<br>knowledge to<br>strengthen our<br>community.</p>
    </article>
    <article class="value">
      <h2>EMPATHY</h2>
      <p>We listen with<br>care, seeking to<br>understand each<br>person’s unique<br>story, feelings,<br>and needs.</p>
    </article>
  </section>
</main>
</body>
</html>
```